Plumbing Website

Design a simple 4 page website based on our provided logo and sketches. Winning designer should be willing to upgrade as needed (for additional fee). A design that includes SEO features is a plus.
I would like to see Home, , Services, Recent Jobs (set up for pictures), Contact. I like the water dropplet back ground. Please dont put logo in a box. File attached as exaple only, I am looking for a request service now button in the middle that will have a form fill to be emailed to two different addresses,
I would like to see vibrant colors. Examples of sites I like are www.brightvalvepipeworks.com look also at www.kmt-keystonemeridianpipes.com - this site is too busy but has good seo features.
Industry/Entity Type
Plumbing
Look and feel

```html
<!DOCTYPE html>
<html lang="en">
<head>
<meta charset="utf-8">
<title>Clearbrook Plumbing</title>
<link href="https://fonts.googleapis.com/css2?family=Play:wght@400;700&family=Arimo:wght@400;700&family=Tinos:ital@1&display=swap" rel="stylesheet">
<style>
:root{
  --brand-blue:#0d5aa7;
  --band-blue:#1b7fc0;
  --accent-red:#e3262c;
  --ink:#333;
  --muted:#666;
  --rule:#d6d6d6;
  --panel:#f4f4f4;
  --dark-btn:#3a3a3a;
  --water-1:#cfe9f8;
  --water-2:#8fcbef;
}
*{box-sizing:border-box;margin:0;padding:0}
html,body{width:1035px;height:1200px;overflow:hidden}
body{font-family:"Arimo",Arial,sans-serif;color:var(--ink);position:relative;background:#fff}
.abs{position:absolute}
.water-bg{left:0;top:117px;width:1035px;height:1083px;
  background:linear-gradient(90deg,var(--water-2) 0%,var(--water-1) 4%,var(--water-2) 8%,var(--water-1) 100%)}
.header{left:0;top:0;width:1035px;height:112px;background:#fff}
.header-band{left:0;top:112px;width:1035px;height:5px;background:var(--band-blue)}
.brand{left:97px;top:40px;display:flex;align-items:center;gap:8px;font-family:"Play",sans-serif;font-weight:700;font-size:24px;color:var(--brand-blue)}
.brand-dot{width:16px;height:16px;border-radius:50%;background:var(--brand-blue)}
.call{right:105px;top:15px;font-size:20px;color:#333}
.follow{left:737px;top:61px;font-family:"Tinos",serif;font-style:italic;font-size:11px;color:#444}
.social{left:816px;top:55px;display:flex;gap:5px}
.social span{width:24px;height:24px;display:block;border-radius:2px}
.nav a{position:absolute;top:95px;font-size:12.5px;color:#222;text-decoration:none}
.nav .current{left:561px;top:92px;width:49px;height:20px;background:var(--band-blue);color:#fff;text-align:center;line-height:20px}
.column{left:90px;top:117px;width:857px;height:1083px;background:#fff}
.hero{left:97px;top:126px;width:841px;height:324px;
  background:linear-gradient(90deg,#5b7fae 0%,#cfd3d8 45%,#e9ebee 100%)}
.arrow{width:40px;height:40px;border-radius:50%;border:3px solid #bbb;background:rgba(255,255,255,.5)}
.cta{left:740px;top:369px;width:160px;height:59px;border:2px solid #fff;border-radius:12px;background:#111;text-align:center;font-family:"Play",sans-serif}
.cta b{display:block;color:var(--accent-red);font-size:21px;margin-top:6px;line-height:22px}
.cta span{color:#fff;font-size:16px}
.rule{left:118px;width:794px;height:1px;background:var(--rule)}
.intro-title{left:90px;width:857px;top:499px;text-align:center;font-family:"Play",sans-serif;font-size:21px;color:var(--accent-red)}
.intro{left:110px;width:817px;top:534px;text-align:center;font-size:10.8px;line-height:15.5px}
.btn{background:var(--dark-btn);color:#fff;font-family:"Play",sans-serif;font-weight:700;font-size:11px;text-align:center}
.readmore{left:481px;top:653px;width:74px;height:21px;line-height:21px}
.service h2{font-family:"Play",sans-serif;font-weight:700;font-size:22px;color:var(--brand-blue);line-height:24px}
.service h3{font-family:"Play",sans-serif;font-weight:700;font-size:11.5px;color:#666;margin-left:2px}
.service .frame{margin-top:10px;width:210px;height:112px;border:1px solid #ddd;padding:5px;background:#fff}
.service .photo{width:100%;height:100%}
.service p{margin-top:14px;width:210px;font-size:10px;line-height:15.5px;text-align:justify}
.vdiv{top:707px;width:0;height:233px;border-left:1px dotted #bbb}
.footer-panel{left:90px;top:949px;width:857px;height:209px;background:var(--panel)}
.footer-panel h4{font-family:"Play",sans-serif;font-weight:700;font-size:16px;color:#666}
.about{left:118px;top:962px;font-size:10.8px;line-height:15.5px;color:#444}
.about b{display:block;margin-top:9px}
.profile{left:381px;top:968px;width:276px;font-size:10.8px;line-height:15.5px}
.profile p{margin-top:14px;text-align:justify}
.enquiry-title{left:729px;top:966px;font-family:"Play",sans-serif;font-weight:700;font-size:22px;color:var(--brand-blue)}
.field{left:724px;width:199px;background:#fff;border:1px solid #ddd;border-radius:3px;font-size:10px;color:#555;padding:6px 9px;line-height:14px}
.submit{left:856px;top:1137px;width:65px;height:21px;line-height:21px}
.foot-nav{left:90px;width:857px;top:1163px;text-align:center;font-size:10px;color:#333;word-spacing:2px}
.foot-nav span{margin:0 12px}
.copy{left:90px;width:857px;top:1180px;text-align:center;font-size:10px;color:#333}
</style>
</head>
<body>
<div class="abs water-bg" role="img" aria-label="Water droplets on a blue surface"></div>

<header class="abs header">
  <div class="abs brand"><span class="brand-dot"></span>Clearbrook Plumbing</div>
  <div class="abs call">Call 555-014-2738</div>
  <div class="abs follow">Follow us on:</div>
  <div class="abs social">
    <span style="background:#3b5a99"></span><span style="background:#2ea3dc"></span><span style="background:#4a8f3a"></span><span style="background:#f08a24"></span>
  </div>
  <nav class="nav">
    <a class="current" href="#">Home</a>
    <a href="#" style="left:641px">Services</a>
    <a href="#" style="left:721px">Recent Jobs</a>
    <a href="#" style="left:835px">Contact</a>
  </nav>
</header>
<div class="abs header-band"></div>

<main class="abs column"></main>

<div class="abs hero" role="img" aria-label="Smiling plumber in a cap kneeling beside pipes under a sink"></div>
<div class="abs arrow" style="left:106px;top:268px"></div>
<div class="abs arrow" style="left:889px;top:268px"></div>
<div class="abs cta"><b>REQUEST</b><span>service now</span></div>

<div class="abs rule" style="top:484px"></div>
<h1 class="abs intro-title">Our Family Serving Your Family</h1>
<div class="abs intro">
  <p>Clearbrook Plumbing is the industry leader in the area. We are a Plumbing, Drain Cleaning, and General Engineering contractors, providing excellent customer service and helping homeowners to live more comfortable and healthy lives. If you are looking for a Plumber in Cedar Valley then call on Clearbrook Plumbing as your Plumbing Contractor. When the water heater bursts or the bathroom is flooding, do you want the best plumber available, or do you want the cheapest? At Clearbrook Plumbing,</p>
  <p style="margin-top:15.5px">we know that the best plumber does world-class work, is fully licensed and insured, is available 24/7 – including during emergencies – and somehow combines world-class equipment and service with world-class affordability.</p>
</div>
<div class="abs btn readmore">Readmore</div>
<div class="abs rule" style="top:685px"></div>

<section class="abs service" style="left:136px;top:702px">
  <h2>Plumbing</h2><h3>simply dummy text</h3>
  <div class="frame" style="margin-left:-3px"><div class="photo" role="img" aria-label="Plumber fixing a bathroom faucet" style="background:linear-gradient(90deg,#d9c9b0,#a88a6a 60%,#2c3550)"></div></div>
  <p>We are a full-service plumbing company. Our plumbers are experts at repairing or replacing all types of leaks,</p>
</section>
<div class="abs vdiv" style="left:374px"></div>
<section class="abs service" style="left:417px;top:702px">
  <h2>Drain Cleaning</h2><h3>simply dummy text</h3>
  <div class="frame" style="margin-left:-12px"><div class="photo" role="img" aria-label="Plumber working on a drain under a kitchen sink" style="background:linear-gradient(90deg,#5d7fb0,#d8dadd 50%,#b39a86)"></div></div>
  <p style="margin-left:-9px">We have been cleaning drains for almost 20 years. Whether it's a kitchen sink or a main sewer line stoppage,</p>
</section>
<div class="abs vdiv" style="left:651px"></div>
<section class="abs service" style="left:687px;top:702px">
  <h2>General Engineering</h2><h3>simply dummy text</h3>
  <div class="frame" style="margin-left:-4px"><div class="photo" role="img" aria-label="Crew cutting into a street with traffic cones" style="background:linear-gradient(180deg,#a9c2d9,#8a8a84 45%,#6e6a62)"></div></div>
  <p style="margin-left:-2px">What sets us apart, is being a class "A" engineering contractor. On larger projects that require cutting concrete and asphalt,</p>
</section>

<footer>
  <div class="abs footer-panel"></div>
  <div class="abs about">
    <h4>About Us</h4>
    <b>Our Office:</b>4210 Meadowlark Ave Suite 210<br>Fairhaven, CA 90017
    <b>Contact Info:</b>555-014-2738<br>service@clearbrookplumbing.com
    <b>24 Hours a Day</b>7 Days a Week
  </div>
  <div class="abs vdiv" style="left:360px;top:963px;height:186px"></div>
  <div class="abs profile">
    <h4>Company Profile</h4>
    <p>When the water heater bursts or the bathroom is flooding, do you want the best plumber available, or do you want the cheapest? At Clearbrook Plumbing, we know that the best plumber does world-class work, is fully licensed and insured, is available 24/7 – including during emergencies – and somehow combines world-class equipment and service with world-class affordability.</p>
  </div>
  <div class="abs vdiv" style="left:685px;top:963px;height:186px"></div>
  <div class="abs enquiry-title">Quick Enquiry</div>
  <div class="abs field" style="top:1005px;height:22px">Your Name</div>
  <div class="abs field" style="top:1038px;height:22px">Email</div>
  <div class="abs field" style="top:1072px;height:56px">Tell Us About Your Project and your Requirment</div>
  <div class="abs btn submit">Submit</div>
  <div class="abs foot-nav">Home<span>~</span>Services<span>~</span>Recent Jobs<span>~</span>Contact</div>
  <div class="abs copy">Copyright © Clearbrook Plumbing . All Rights Reserved</div>
</footer>
</body>
</html>
```